Hawaiian Entertainment Booking Business needs a logo design/business card

We need a logo design/business card for a Hawaii based entertainment company called "Malvera Studios". We book all types of entertainment--musicians, bands, hula dancers, fire-knife dancers, halau, etc. for venues, events, weddings, parties, conventions. We would like to see designs that are cool, artistic, yet classy.

Industry/Entity Type

Entertainment Industry

Contact Information for Business Card

Leilani Kahuenga
Malvera Studios, LLC
P.O. Box 47213
Honolulu, HI 96822
(808)555-0147

Colors
acd036

Requirements
Must have
• Must say somewhere on card: Entertainment Services
Nice to have
• Please highlight: Leilani Kahuenga

```html
<!DOCTYPE html>
<html lang="en">
<head>
<meta charset="utf-8">
<title>Malvera Studios – Business Card</title>
<link rel="stylesheet" href="https://fonts.googleapis.com/css2?family=Oswald:wght@600&family=Raleway:wght@400;700&display=swap">
<style>
  :root {
    --stage: #262626;
    --card-black: #050608;
    --glow-blue: #1b2a52;
    --swoosh-blue: #1f97c4;
    --band-white: #f4f4f4;
    --band-text: #1e5f80;
    --text-white: #ffffff;
    --icon-blue: #1f97c4;
    --art-teal: #2aa6cf;
    --art-yellow: #f2c21b;
    --art-orange: #f07a1e;
    --art-red: #e8321c;
  }
  * { margin: 0; padding: 0; box-sizing: border-box; }
  html, body { width: 1200px; height: 800px; overflow: hidden; }
  body { background: var(--stage); position: relative; }

  .business-card {
    position: absolute;
    left: 150px; top: 143px;
    width: 900px; height: 514px;
    border-radius: 28px;
    overflow: hidden;
    background:
      radial-gradient(ellipse 320px 200px at 52% 50%, var(--glow-blue), transparent 75%),
      var(--card-black);
  }
  .card-shapes { position: absolute; inset: 0; }

  .tagline {
    position: absolute;
    left: 38px; top: 34px;
    font-family: "Oswald", sans-serif;
    font-weight: 600;
    font-size: 36px;
    letter-spacing: 0.5px;
    color: var(--band-text);
    text-transform: uppercase;
  }

  .brand-art {
    position: absolute;
    right: 48px; top: 120px;
    width: 230px; height: 150px;
    border-radius: 6px;
    background: linear-gradient(90deg, var(--art-teal) 0%, var(--art-yellow) 40%, var(--art-orange) 72%, var(--art-red) 100%);
  }
  .brand-name {
    position: absolute;
    right: 48px; top: 276px;
    width: 230px;
    text-align: center;
    font-family: "Raleway", sans-serif;
    font-weight: 400;
    font-size: 26px;
    letter-spacing: 2px;
    color: var(--text-white);
  }

  .contact {
    position: absolute;
    right: 48px; top: 330px;
    text-align: right;
    font-family: "Raleway", sans-serif;
    color: var(--text-white);
  }
  .contact .person-name {
    font-weight: 700;
    font-size: 34px;
    letter-spacing: 0.5px;
    margin-bottom: 6px;
  }
  .contact .line {
    font-weight: 400;
    font-size: 25px;
    line-height: 34px;
    display: flex;
    justify-content: flex-end;
    align-items: center;
    gap: 12px;
  }
  .contact .line.no-icon { padding-right: 38px; }
  .icon { width: 26px; height: 26px; flex: none; }
</style>
</head>
<body>
  <div class="business-card">
    <svg class="card-shapes" width="900" height="514" viewBox="0 0 900 514" aria-hidden="true">
      <!-- white tagline band -->
      <path d="M0,24 L530,24 C580,24 610,60 640,82 C652,92 648,100 632,100 L560,96 C540,96 520,92 0,92 Z" fill="var(--band-white)"/>
      <!-- main blue swoosh -->
      <path d="M680,60 C560,110 300,200 120,330 C80,360 50,400 20,460 C90,390 160,340 260,285 C420,200 570,120 680,60 Z" fill="var(--swoosh-blue)"/>
      <!-- inner swoosh -->
      <path d="M420,150 C300,170 150,220 40,290 L0,320 L0,345 C120,260 260,195 420,150 Z" fill="var(--swoosh-blue)"/>
      <!-- left edge accents -->
      <path d="M0,225 C40,215 70,210 90,208 C60,225 30,245 0,265 Z" fill="var(--swoosh-blue)"/>
      <path d="M0,395 C30,370 60,350 90,335 C60,365 30,400 10,440 L0,440 Z" fill="var(--swoosh-blue)"/>
    </svg>

    <div class="tagline">Entertainment Services</div>

    <div class="brand-art" role="img" aria-label="Illustration of a hula dancer with palm trees and a setting sun"></div>
    <div class="brand-name">MALVERA STUDIOS</div>

    <div class="contact">
      <div class="person-name">Leilani Kahuenga</div>
      <div class="line">(808)555-0147
        <svg class="icon" viewBox="0 0 26 26" aria-hidden="true">
          <circle cx="13" cy="13" r="13" fill="var(--icon-blue)"/>
          <path d="M9,7 L11,7 L12,10.5 L10.6,11.8 C11.3,13.4 12.6,14.7 14.2,15.4 L15.5,14 L19,15 L19,17 C19,18 18,19 17,19 C12,19 7,14 7,9 C7,8 8,7 9,7 Z" fill="var(--card-black)"/>
        </svg>
      </div>
      <div class="line">P.O. Box 47213
        <svg class="icon" viewBox="0 0 26 26" aria-hidden="true">
          <circle cx="13" cy="13" r="13" fill="var(--icon-blue)"/>
          <path d="M13,6 L20,12.5 L18,12.5 L18,19 L14.5,19 L14.5,15 L11.5,15 L11.5,19 L8,19 L8,12.5 L6,12.5 Z" fill="var(--card-black)"/>
        </svg>
      </div>
      <div class="line no-icon">Honolulu, HI 96822</div>
    </div>
  </div>
</body>
</html>
```